farvinta labs cybersecurity website design and development

website design and development for a cybersecurity company. we have a logo and would like site to suit logo colors and look
cybersecurity website should be secure and look professional
main example of site we want to use: https://www.plomvex.example/
site should be usable on tablet and phones

For each design proposal, please could you provide details of what language you'll use to code the website.

Target Market(s)

insurance companies, financial institutions, private SME, Africa and Europe

Coding

Coded - Design and coding required

Number of Pages Required

5+ page

Requirements
Must have
• 9 Pages:
Home
About us
Contacts
Partners
Blog
Services
( consulting, vulnerability assessment, information systems security audit, ISO compliance, Penetration testing, security awareness training, social engineering test, protection against DDoS, procurement )
Resources
Technologies
Careers
Nice to have
• nice to have all services have their own pages.
design based on logo colors and look

please provide what will be use to code the website

```html
<!DOCTYPE html>
<html lang="en">
<head>
<meta charset="utf-8">
<title>Farvinta Labs — Cybersecurity</title>
<link rel="stylesheet" href="https://fonts.googleapis.com/css2?family=Barlow:wght@400;500;600&family=Barlow+Semi+Condensed:wght@500;600&display=swap">
<style>
  :root {
    --stage: #88a0ad;
    --card: #ffffff;
    --strip: #e2eef7;
    --slate: #8aa0ad;
    --ink: #2d3338;
    --navy: #1b3a8f;
    --azure: #0a9be0;
    --dot: #e2eef7;
    --dot-active: #8aa0ad;
    --client: #3c4449;
    --footer: #88a0ad;
    --footer-text: #ffffff;
    --photo-warm: #d7a27c;
    --photo-dark: #3a2619;
  }
  * { margin: 0; padding: 0; box-sizing: border-box; }
  html, body { width: 766px; height: 1200px; overflow: hidden; background: var(--stage); }
  body { position: relative; font-family: "Barlow", Arial, sans-serif; color: var(--ink); }

  .page { position: absolute; left: 67px; top: 38px; width: 631px; height: 1124px; background: var(--card); overflow: hidden; }
  .side-strip { position: absolute; left: 0; top: 0; width: 44px; height: 961px; background: var(--strip); }
  .abs { position: absolute; }

  .brand { left: 25px; top: 30px; display: flex; align-items: center; gap: 5px; }
  .brand-mark { width: 18px; height: 18px; border-radius: 50%; background: var(--navy); }
  .brand-name { font-family: "Barlow Semi Condensed", Arial, sans-serif; font-weight: 600; font-size: 14px; color: var(--navy); }

  .nav a { position: absolute; top: 34px; font-family: "Barlow Semi Condensed", Arial, sans-serif; font-weight: 600; font-size: 6.6px; color: var(--slate); text-decoration: none; letter-spacing: .1px; }

  .hero-photo { left: 168px; top: 70px; width: 463px; height: 271px; border-top-left-radius: 22px;
    background: linear-gradient(100deg, var(--photo-warm) 0%, #a97555 50%, var(--photo-dark) 100%); }
  .hero-title { left: 61px; top: 133px; font-family: "Barlow Semi Condensed", Arial, sans-serif; font-weight: 600; font-size: 33.5px; line-height: 27px; color: var(--slate); white-space: nowrap; }
  .hero-copy { left: 62px; top: 199px; font-size: 7px; line-height: 9px; color: var(--ink); white-space: nowrap; }
  .hero-copy p + p { margin-top: 8px; }
  .btn { left: 63px; top: 256px; width: 119px; height: 22px; border-radius: 4px;
    background: linear-gradient(90deg, var(--navy), var(--azure)); color: #fff; font-family: "Barlow Semi Condensed", Arial, sans-serif; font-weight: 500; font-size: 10.5px; display: flex; align-items: center; justify-content: center; }

  .dots { display: flex; gap: 4px; }
  .dots span { width: 7.5px; height: 7.5px; background: var(--dot); }
  .dots span.on { background: var(--dot-active); }

  .heading { font-family: "Barlow Semi Condensed", Arial, sans-serif; font-weight: 500; font-size: 24.7px; line-height: 26.4px; color: var(--slate); white-space: nowrap; }
  .body-text { font-size: 6.7px; line-height: 8.8px; color: var(--ink); white-space: nowrap; }

  .rule { left: 168px; top: 527px; width: 463px; height: 1.5px; background: var(--strip); }
  .cert-badge { left: 82px; top: 570px; width: 50px; height: 48px; border-radius: 50%; background: linear-gradient(150deg, #c9d8e3, #1b62c4); }

  .standards-band { left: 0; top: 673px; width: 464px; height: 105px; border-top-right-radius: 22px;
    background: linear-gradient(60deg, var(--navy) 0%, #0e6abf 50%, var(--azure) 100%); }
  .badge { position: absolute; width: 80px; text-align: center; font-size: 6.4px; line-height: 8px; }
  .badge i { display: block; width: 33px; height: 33px; margin: 0 auto 10px; border-radius: 50%; }
  .standards-band .badge { color: #fff; top: 26px; }
  .standards-band .badge i { background: var(--strip); }
  .clients .badge { color: var(--ink); }
  .clients .badge i { background: var(--client); }

  .footer { left: 0; top: 961px; width: 631px; height: 163px; background: var(--footer); color: var(--footer-text); }
  .foot-col { position: absolute; top: 18px; font-size: 6px; }
  .foot-col h4 { font-family: "Barlow Semi Condensed", Arial, sans-serif; font-weight: 600; font-size: 6.6px; margin-bottom: 12px; }
  .foot-col li { list-style: none; height: 13.2px; }
  .foot-rule { position: absolute; left: 44px; top: 123px; width: 587px; height: 1px; background: #d8e2e8; }
  .foot-copy { position: absolute; top: 133px; font-size: 10px; line-height: 14px; white-space: nowrap; }
  .social { position: absolute; top: 134px; width: 13px; height: 13px; border-radius: 50%; background: var(--footer-text); }
</style>
</head>
<body>
<main class="page">
  <div class="side-strip"></div>

  <div class="abs brand"><span class="brand-mark"></span><span class="brand-name">Farvinta Labs</span></div>

  <nav class="nav">
    <a style="left:192px">HOME</a>
    <a style="left:227px">ABOUT US</a>
    <a style="left:275px">CONTACTS</a>
    <a style="left:324px">PARTNERS</a>
    <a style="left:373px">BLOG</a>
    <a style="left:406px">SERVICES</a>
    <a style="left:453px">RESOURCES</a>
    <a style="left:506px">TECHNOLOGIES</a>
    <a style="left:569px">CAREERS</a>
  </nav>

  <div class="abs hero-photo" role="img" aria-label="Photo: hands typing on a laptop keyboard with a digital security shield overlay"></div>
  <h1 class="abs hero-title">ARE YOU<br>CYBERSECURE?</h1>
  <div class="abs hero-copy">
    <p>Would you be able to detect<br>automated or targeted attacks?</p>
    <p>Do you know if have you<br>already been a victim?</p>
  </div>
  <a class="abs btn">LEARN MORE</a>
  <div class="abs dots" style="left:120px;top:333px"><span></span><span class="on"></span><span></span><span></span></div>

  <h2 class="abs heading" style="left:168px;top:368px">We make sure our clients<br>stay ahead of attacks and mitigate<br>future risks</h2>
  <p class="abs body-text" style="left:168px;top:455px">Lorem ipsum dolor sit amet, consectetuer adipiscing elit, sed diam nonummy nibh euismod tincid-<br>unt ut laoreet dolore magna aliquam erat volutpat. Ut wisi enim ad minim veniam, quis nostrud<br>exerci tation ullamcorper suscipit lobortis nisl ut aliquip ex ea commodo consequat. Duis autem vel<br>eum iriure dolor in hendrerit in vulputate velit esse molestie consequat, vel illum dolore eu feugiat<br>nulla facilisis at vero eros et accumsan et iusto odio dignissim qui blandit praesent luptatum zzril<br>delenit augue duis dolore te feugait nulla facilisi.</p>

  <div class="abs rule"></div>

  <div class="abs cert-badge" role="img" aria-label="Certification badge"></div>
  <h2 class="abs heading" style="left:169px;top:554px">Farvinta Labs is certified<br>by the international quality standards<br>ISO 20000, ISO 27001 and ISO 9001</h2>
  <p class="abs body-text" style="left:168px;top:640px">Our team of experts are certified by some of the top security organizations and vendors in the<br>industry - Verisol, Kestrel Institute, Norvane Board, Redmark Academy and more.</p>

  <section class="abs standards-band">
    <div class="badge" style="left:66px"><i></i>LOGO/MARK<br>QUALITY STADARD</div>
    <div class="badge" style="left:162px"><i></i>LOGO/MARK<br>QUALITY STADARD</div>
    <div class="badge" style="left:257px"><i></i>LOGO/MARK<br>QUALITY STADARD</div>
    <div class="badge" style="left:352px"><i></i>LOGO/MARK<br>QUALITY STADARD</div>
  </section>
  <div class="abs dots" style="left:470px;top:769px"><span></span><span class="on"></span><span></span><span></span></div>

  <h2 class="abs heading" style="left:168px;top:810px">They already trusted us</h2>
  <section class="clients">
    <div class="badge" style="left:66px;top:856px"><i></i>LOGO/MARK<br>QUALITY STADARD</div>
    <div class="badge" style="left:162px;top:856px"><i></i>LOGO/MARK<br>QUALITY STADARD</div>
    <div class="badge" style="left:257px;top:856px"><i></i>LOGO/MARK<br>QUALITY STADARD</div>
    <div class="badge" style="left:352px;top:856px"><i></i>LOGO/MARK<br>QUALITY STADARD</div>
    <div class="badge" style="left:448px;top:856px"><i></i>LOGO/MARK<br>QUALITY STADARD</div>
  </section>
  <svg class="abs" style="left:563px;top:868px" width="10" height="10" viewBox="0 0 10 10"><path d="M1 0 L10 5 L1 10 Z" fill="#8aa0ad"/></svg>

  <footer class="abs footer">
    <div class="foot-col" style="left:60px"><h4>SERVICES</h4><ul><li>Lorem ipsum</li><li>Lorem ipsum</li><li>Lorem ipsum</li><li>Lorem ipsum</li></ul></div>
    <div class="foot-col" style="left:168px"><h4>RESOURCES</h4><ul><li>Lorem ipsum</li><li>Lorem ipsum</li><li>Lorem ipsum</li><li>Lorem ipsum</li><li>Lorem ipsum</li></ul></div>
    <div class="foot-col" style="left:272px"><h4>TECHNOLOGIES</h4><ul><li>Lorem ipsum</li><li>Lorem ipsum</li><li>Lorem ipsum</li></ul></div>
    <div class="foot-col" style="left:464px"><h4>GET IN TOUCH</h4></div>
    <div class="foot-rule"></div>
    <span class="foot-copy" style="left:61px">© 2021</span>
    <span class="foot-copy" style="left:102px">Farvinta Labs</span>
    <span class="social" style="left:172px" aria-label="Social link"></span>
    <span class="social" style="left:207px" aria-label="Social link"></span>
    <span class="social" style="left:240px" aria-label="Social link"></span>
  </footer>
</main>
</body>
</html>
```